Design a premium label for the most expensive honey in the world: Manuka honey.

Manuka honey is originaire from New Zealand and recognized for its natural antibacterial activity. Rare and expensive, it is used in hospital as medical grade mainly to cure burns and wounds... Household will use it out of a pot like a "supplement" or to cure all sorts of ailments.
The label must feel:
- Premium and elegant .
- Reflect strongly its origin New Zealand. Use maori design but be careful of copyright. Must be styled.
- Purity and trust it is the real deal. Feel strongly that it is not an ersatz...
- Health and "medical" use.
Label must have:
* Brand: TOROWAI DOWNS
* MANUKA HONEY
* Made in New Zealand
* e250g
* MGO300
Target Market(s)
Export.

```html
<!DOCTYPE html>
<html lang="en">
<head>
<meta charset="utf-8">
<title>Torowai Downs Manuka Honey – Jar Label</title>
<link rel="stylesheet" href="https://fonts.googleapis.com/css2?family=Exo+2:wght@500;600;700;800&display=swap">
<style>
  :root {
    --stage: #e4e4e4;
    --label-dark: #2a2a2b;
    --label-swirl: #3a3a3c;
    --gold: #d6a93a;
    --ink-dark: #1f1f1f;
    --ink-light: #ffffff;
  }
  html, body {
    margin: 0;
    padding: 0;
    width: 1123px;
    height: 1200px;
    overflow: hidden;
    background: var(--stage);
  }
  .canvas {
    position: relative;
    width: 1123px;
    height: 1200px;
  }
  .label {
    position: absolute;
    left: 40px;
    top: 432px;
    width: 1043px;
    height: 335px;
    display: block;
  }
  .label text {
    font-family: "Exo 2", sans-serif;
  }
  .brand-name { fill: var(--ink-dark); font-weight: 700; font-size: 19px; }
  .product-title { fill: var(--gold); font-weight: 800; font-size: 64px; }
  .product-subtitle { fill: var(--gold); font-weight: 700; font-size: 44px; }
  .origin-line { fill: var(--ink-dark); font-weight: 600; font-size: 14.5px; }
  .spec-line { fill: var(--ink-light); font-weight: 600; font-size: 18px; }
  .side-copy { fill: var(--ink-light); font-weight: 600; font-size: 17.5px; }
</style>
</head>
<body>
<main class="canvas">
  <svg class="label" viewBox="0 0 1043 335" xmlns="http://www.w3.org/2000/svg">
    <defs>
      <radialGradient id="swirl-tone" cx="50%" cy="50%" r="70%">
        <stop offset="0%" stop-color="var(--label-swirl)"/>
        <stop offset="100%" stop-color="var(--label-dark)"/>
      </radialGradient>
      <path id="title-arc" d="M 352 232 Q 521 80 690 232"/>
    </defs>

    <rect class="label-pattern" role="img" aria-label="Maori-inspired koru swirl pattern in charcoal tones"
          x="0" y="0" width="1043" height="335" fill="url(#swirl-tone)" stroke="#111" stroke-width="2"/>

    <!-- brand tab -->
    <path class="brand-tab" d="M 444 0 L 599 0 L 599 10 A 77.5 66 0 0 1 444 10 Z" fill="var(--gold)"/>
    <text class="brand-name" x="521.5" y="37" text-anchor="middle">TOROWAI</text>
    <text class="brand-name" x="521.5" y="58" text-anchor="middle">DOWNS</text>

    <!-- title -->
    <text class="product-title"><textPath href="#title-arc" startOffset="50%" text-anchor="middle">MANUKA</textPath></text>
    <text class="product-subtitle" x="521.5" y="227" text-anchor="middle">HONEY</text>

    <!-- origin band -->
    <path class="origin-band" d="M 388 288 L 388 276 Q 388 264 400 264 L 643 264 Q 655 264 655 276 L 655 288 Z" fill="var(--gold)"/>
    <text class="origin-line" x="521.5" y="281" text-anchor="middle">Made and packed in New Zealand</text>
    <text class="spec-line" x="521.5" y="311" text-anchor="middle">e250g | MGO300</text>

    <!-- left panel -->
    <g class="side-panel side-panel--left">
      <text class="side-copy" text-anchor="middle">
        <tspan x="177" y="65">Lorem ipsum dolor sit amet,</tspan>
        <tspan x="177" y="86">consectetuer adipiscing elit, sed</tspan>
        <tspan x="177" y="107">diam nonummy nibh euismod</tspan>
        <tspan x="177" y="128">tincidunt ut laoreet dolore magna</tspan>
        <tspan x="177" y="149">aliquam erat volutpat. Ut wisi</tspan>
        <tspan x="177" y="170">enim ad minim veniam, quis</tspan>
      </text>
      <rect class="info-box" x="49" y="218" width="256" height="66" fill="var(--ink-light)"/>
    </g>

    <!-- right panel -->
    <g class="side-panel side-panel--right">
      <text class="side-copy" text-anchor="middle">
        <tspan x="863" y="65">Lorem ipsum dolor sit amet,</tspan>
        <tspan x="863" y="86">consectetuer adipiscing elit, sed</tspan>
        <tspan x="863" y="107">diam nonummy nibh euismod</tspan>
        <tspan x="863" y="128">tincidunt ut laoreet dolore magna</tspan>
        <tspan x="863" y="149">aliquam erat volutpat. Ut wisi</tspan>
        <tspan x="863" y="170">enim ad minim veniam, quis</tspan>
      </text>
      <rect class="info-box" x="743" y="218" width="256" height="66" fill="var(--ink-light)"/>
    </g>
  </svg>
</main>
</body>
</html>
```